Verimo Cleaning Company Flyer

Hi, We need an A4 flyer design for our cleaning company, focusing on dry carpet cleaning I attached our catalogue to give some idea. In addition, our websites can provide more information. Our Services:-General Cleaning Carry out heavy cleansing tasks and special projects. Clean, stock and supply designated facility areas (dusting, sweeping, vacuuming, mopping, cleaning ceiling vents, restroom cleaning etc).Using electrically powered scrubbing and polishing machines to burnish, scrub, polish and spray clean floors. Window Cleaning Regular, Reliable Window Cleaning.Hard To Reach Windows.Single 7 Multi-Storey.Frames and Glass Cleaned.Floor Cleaning Cleaning Marble Cleaning & Polishing.Tile & Grout Cleaning.Hardwood Floors Services.Vinyl Floors.The PELKA Dry Extraction Carpet Cleaning System uses environmentally preferred, Amber Crest Certified cleaning products that deep cleans your carpets and textured hard floors quickly and easily.

Target Market(s)

Commercial Cleaning residential Cleaning Hotel cleaning

Industry/Entity Type

Cleaning Service

Contact Information for Business Card

Tariq Hamdan Al-Saeedi Gm
Derek Olmo Marketing Manger

Font styles to use
Serif
Sans Serif

Colors
0355a3
3176b5
85acd3
cee9f5
85cae6
34a6d7
0592cd

```html
<!DOCTYPE html>
<html lang="en">
<head>
<meta charset="utf-8">
<title>Verimo Cleaning – Dry Carpet Cleaning Flyer</title>
<link href="https://fonts.googleapis.com/css2?family=Montserrat:wght@400;500;600;700;800&display=swap" rel="stylesheet">
<style>
  :root {
    --navy: #0355a3;
    --deep: #0b3f7a;
    --mid-blue: #3176b5;
    --soft-blue: #85acd3;
    --ice: #cee9f5;
    --sky: #85cae6;
    --bright: #34a6d7;
    --cyan: #0592cd;
    --ink: #1d2c44;
    --page-bg: #e9ecef;
    --white: #ffffff;
  }
  * { box-sizing: border-box; margin: 0; padding: 0; }
  html, body { width: 1200px; height: 1200px; overflow: hidden; }
  body {
    background: var(--page-bg);
    font-family: "Montserrat", Arial, sans-serif;
    color: var(--ink);
    position: relative;
  }
  .flyer {
    position: absolute;
    left: 210px; top: 34px;
    width: 780px; height: 1132px;
    background: var(--white);
    overflow: hidden;
    box-shadow: 0 10px 30px rgba(0,0,0,.18);
  }
  .hero-photo {
    position: absolute; left: 0; top: 0;
    width: 780px; height: 640px;
    background: linear-gradient(135deg, #a8683a 0%, #8a4f29 40%, #6e3a1c 70%, #b27a45 100%);
  }
  .shape-layer { position: absolute; left: 0; top: 0; width: 780px; height: 1132px; }
  .brand {
    position: absolute; left: 430px; top: 34px;
    font-weight: 700; font-size: 30px; color: var(--navy);
    display: flex; align-items: center; gap: 10px;
  }
  .brand-dot { width: 16px; height: 16px; border-radius: 50%; background: var(--bright); }
  .headline {
    position: absolute; left: 40px; top: 640px;
    font-weight: 800; font-size: 50px; letter-spacing: 2px; color: var(--navy);
    line-height: 1;
  }
  .headline .accent { color: var(--bright); }
  .services-tag {
    position: absolute; left: 28px; top: 708px;
    background: var(--navy); color: var(--white);
    font-weight: 700; font-size: 20px; letter-spacing: 1px;
    padding: 6px 22px 6px 20px; border-radius: 0 20px 20px 0;
  }
  .services-intro {
    position: absolute; left: 40px; top: 752px; width: 470px;
    font-size: 14px; line-height: 1.35; font-weight: 500;
  }
  .service-list {
    position: absolute; list-style: none;
    font-size: 15px; font-weight: 500;
  }
  .service-list li { display: flex; align-items: center; gap: 10px; height: 25px; }
  .service-list svg { width: 14px; height: 14px; flex: none; }
  .list-left { left: 44px; top: 798px; }
  .list-right { left: 250px; top: 798px; }
  .equipment-photo {
    position: absolute; left: 540px; top: 686px; width: 210px; height: 150px;
    background: linear-gradient(160deg, #e4e9f1 0%, #7d8aa3 55%, #2c3d66 100%);
    border-radius: 4px;
  }
  .pelka-copy {
    position: absolute; left: 530px; top: 850px; width: 232px;
    font-size: 12.5px; line-height: 1.4; font-weight: 500;
  }
  .machines-copy {
    position: absolute; left: 40px; top: 954px; width: 470px;
    font-size: 14px; line-height: 1.35; font-weight: 500;
  }
  .windows-title {
    position: absolute; left: 40px; top: 1000px;
    font-weight: 700; font-size: 17px; color: var(--navy); letter-spacing: .5px;
  }
  .windows-copy {
    position: absolute; left: 40px; top: 1023px; width: 420px;
    font-size: 14px; line-height: 1.35; font-weight: 500;
  }
  .partner-mark {
    position: absolute; left: 600px; top: 994px;
    font-weight: 700; font-size: 34px; color: var(--navy);
  }
  .contact {
    position: absolute; display: flex; align-items: center; gap: 10px;
    font-size: 15px; font-weight: 600;
  }
  .contact svg { width: 20px; height: 20px; }
  .contact-phone { left: 60px; top: 1098px; color: var(--white); }
  .contact-web { left: 300px; top: 1098px; color: var(--white); }
</style>
</head>
<body>
  <main class="flyer">
    <div class="hero-photo" role="img" aria-label="Photo of a uniformed cleaner wiping and polishing a large carved wooden door"></div>

    <svg class="shape-layer" viewBox="0 0 780 1132" aria-hidden="true">
      <path d="M0 0 H780 V90 C620 120 470 118 330 70 C230 38 110 30 0 40 Z" fill="#ffffff"/>
      <path d="M330 70 C470 118 620 120 780 90" fill="none" stroke="#34a6d7" stroke-width="5"/>
      <path d="M0 640 C260 600 520 570 780 548 V1132 H0 Z" fill="#ffffff"/>
      <path d="M0 632 C260 592 520 562 780 540" fill="none" stroke="#0355a3" stroke-width="6"/>
      <path d="M0 641 C260 601 520 571 780 549" fill="none" stroke="#34a6d7" stroke-width="4"/>
      <path d="M0 1090 C260 1084 520 1064 780 1024 V1132 H0 Z" fill="#0355a3"/>
      <path d="M0 1082 C260 1076 520 1056 780 1016" fill="none" stroke="#34a6d7" stroke-width="4"/>
      <ellipse cx="665" cy="1030" rx="112" ry="42" fill="#ffffff"/>
    </svg>

    <div class="brand"><span class="brand-dot"></span>Verimo Cleaning</div>

    <h1 class="headline">DRY CARPET <span class="accent">CLEANING</span></h1>
    <div class="services-tag">OUR SERVICES:</div>
    <p class="services-intro">General Cleaning Carry out heavy cleansing tasks &amp; special projects. Clean, stock and supply designated facility areas</p>

    <ul class="service-list list-left">
      <li><svg viewBox="0 0 14 14"><circle cx="7" cy="7" r="7" fill="#0592cd"/><path d="M4 7.2 6.2 9.3 10.2 5" fill="none" stroke="#fff" stroke-width="1.8"/></svg>Dusting</li>
      <li><svg viewBox="0 0 14 14"><circle cx="7" cy="7" r="7" fill="#0592cd"/><path d="M4 7.2 6.2 9.3 10.2 5" fill="none" stroke="#fff" stroke-width="1.8"/></svg>Sweeping</li>
      <li><svg viewBox="0 0 14 14"><circle cx="7" cy="7" r="7" fill="#0592cd"/><path d="M4 7.2 6.2 9.3 10.2 5" fill="none" stroke="#fff" stroke-width="1.8"/></svg>Mopping</li>
      <li><svg viewBox="0 0 14 14"><circle cx="7" cy="7" r="7" fill="#0592cd"/><path d="M4 7.2 6.2 9.3 10.2 5" fill="none" stroke="#fff" stroke-width="1.8"/></svg>Vacuuming</li>
      <li><svg viewBox="0 0 14 14"><circle cx="7" cy="7" r="7" fill="#0592cd"/><path d="M4 7.2 6.2 9.3 10.2 5" fill="none" stroke="#fff" stroke-width="1.8"/></svg>Vinyl Floors</li>
      <li><svg viewBox="0 0 14 14"><circle cx="7" cy="7" r="7" fill="#0592cd"/><path d="M4 7.2 6.2 9.3 10.2 5" fill="none" stroke="#fff" stroke-width="1.8"/></svg>Floor Cleaning</li>
    </ul>
    <ul class="service-list list-right">
      <li><svg viewBox="0 0 14 14"><circle cx="7" cy="7" r="7" fill="#0592cd"/><path d="M4 7.2 6.2 9.3 10.2 5" fill="none" stroke="#fff" stroke-width="1.8"/></svg>Cleaning ceiling vents</li>
      <li><svg viewBox="0 0 14 14"><circle cx="7" cy="7" r="7" fill="#0592cd"/><path d="M4 7.2 6.2 9.3 10.2 5" fill="none" stroke="#fff" stroke-width="1.8"/></svg>Restroom cleaning</li>
      <li><svg viewBox="0 0 14 14"><circle cx="7" cy="7" r="7" fill="#0592cd"/><path d="M4 7.2 6.2 9.3 10.2 5" fill="none" stroke="#fff" stroke-width="1.8"/></svg>Tile &amp; Grout Cleaning.</li>
      <li><svg viewBox="0 0 14 14"><circle cx="7" cy="7" r="7" fill="#0592cd"/><path d="M4 7.2 6.2 9.3 10.2 5" fill="none" stroke="#fff" stroke-width="1.8"/></svg>Marble Cleaning &amp; Polishing</li>
      <li><svg viewBox="0 0 14 14"><circle cx="7" cy="7" r="7" fill="#0592cd"/><path d="M4 7.2 6.2 9.3 10.2 5" fill="none" stroke="#fff" stroke-width="1.8"/></svg>Hardwood Floors Services.</li>
    </ul>

    <div class="equipment-photo" role="img" aria-label="Product shot of dry extraction carpet cleaning machines and supply buckets"></div>
    <p class="pelka-copy">The PELKA Dry Extraction Carpet Cleaning System uses environmentally preferred, Amber Crest Certified cleaning products that deep cleans your carpets and textured hard floors quickly and easily.</p>

    <p class="machines-copy">Using electrically powered scrubbing and polishing machines to burnish, scrub, polish &amp; spray clean floors.</p>
    <h2 class="windows-title">HARD TO REACH WINDOWS!</h2>
    <p class="windows-copy">Window Cleaning Regular, Reliable Window Cleaning.<br>Single 7 Multi-Storey.Frames and Glass Cleaned.</p>

    <div class="partner-mark">PELKA</div>

    <div class="contact contact-phone">
      <svg viewBox="0 0 20 20"><path d="M5 2.5 8 5.5 6.5 8c1 2.2 3.3 4.5 5.5 5.5L14.5 12l3 3-2 2.5C9 17 3 11 2.5 4.5Z" fill="#85cae6"/></svg>
      +974-4000-1257
    </div>
    <div class="contact contact-web">
      <svg viewBox="0 0 20 20"><g fill="none" stroke="#85cae6" stroke-width="1.6"><circle cx="10" cy="10" r="8"/><ellipse cx="10" cy="10" rx="3.5" ry="8"/><path d="M2 10h16M3.5 6h13M3.5 14h13"/></g></svg>
      www.verimocleaning1993.business.site
    </div>
  </main>
</body>
</html>
```